Business Card for Technology Startup

Design a 2-sided business card using the logo provided. We are a digital healthcare platform that provides a mobile app and web UI that helps caregivers, families, and doctors share information and provide better patient outcomes. We use AI and machine learning to help guide patients through their day-to-day life. The final design should communicate stability, peace, comfort, but also align with the image of an AI-driven technology startup.

I'd like the deliverable to by a Photoshop PSD file (with layers) that I can work with in pixlr.com. Should contain the following editable layers:
Name (ex. John Doe)
Title (ex. Founder / CEO)
Email (ex. info@brenvaxa.ai)
Phone (ex. (555) 014-2290)
Website (ex. https://brenvaxa.ai)

```html
<!DOCTYPE html>
<html lang="en">
<head>
<meta charset="utf-8">
<title>Brenvaxa Business Card</title>
<link rel="stylesheet" href="https://fonts.googleapis.com/css2?family=Montserrat:wght@400;500;800&display=swap">
<style>
  :root {
    --backdrop: #2b2b2b;
    --card: #161616;
    --white: #ffffff;
    --cyan: #27bfe6;
    --cyan-soft: #5fd0ec;
  }
  * { margin: 0; padding: 0; box-sizing: border-box; }
  html, body { width: 1200px; height: 689px; overflow: hidden; }
  body {
    background: var(--backdrop);
    font-family: "Montserrat", Arial, sans-serif;
    color: var(--white);
    position: relative;
  }
  .card {
    position: absolute;
    top: 190px;
    width: 540px;
    height: 309px;
    background: var(--card);
    border-radius: 22px;
    overflow: hidden;
  }
  .card--front { left: 40px; }
  .card--back { left: 620px; }

  /* Front */
  .front-brand {
    position: absolute;
    left: 52px;
    top: 50%;
    transform: translateY(-50%);
    display: flex;
    align-items: center;
    gap: 26px;
  }
  .brand-dot {
    border-radius: 50%;
    background: linear-gradient(135deg, var(--cyan) 0%, var(--cyan-soft) 100%);
    flex: none;
  }
  .front-brand .brand-dot { width: 96px; height: 96px; }
  .brand-name {
    font-weight: 800;
    color: var(--white);
    letter-spacing: 0.5px;
    line-height: 1;
  }
  .front-brand .brand-name { font-size: 64px; }

  /* Back */
  .back-brand {
    position: absolute;
    left: 34px;
    top: 50%;
    transform: translateY(-50%);
    display: flex;
    align-items: center;
    gap: 10px;
  }
  .back-brand .brand-dot { width: 22px; height: 22px; }
  .back-brand .brand-name { font-size: 28px; }
  .divider {
    position: absolute;
    left: 262px;
    top: 62px;
    width: 2px;
    height: 185px;
    background: var(--cyan);
  }
  .contact-block {
    position: absolute;
    left: 284px;
    top: 66px;
  }
  .person-name {
    font-weight: 800;
    font-size: 27px;
    color: var(--cyan);
    line-height: 1.1;
  }
  .person-title {
    font-weight: 400;
    font-size: 15px;
    margin-top: 4px;
  }
  .contact-list {
    list-style: none;
    margin-top: 26px;
  }
  .contact-item {
    display: flex;
    align-items: center;
    gap: 9px;
    font-size: 13.5px;
    font-weight: 400;
    line-height: 1;
    margin-bottom: 11px;
  }
  .contact-icon { width: 13px; height: 13px; flex: none; fill: var(--cyan); }
</style>
</head>
<body>
  <section class="card card--front" aria-label="Card front">
    <div class="front-brand">
      <span class="brand-dot"></span>
      <span class="brand-name">brenvaxa</span>
    </div>
  </section>

  <section class="card card--back" aria-label="Card back">
    <div class="back-brand">
      <span class="brand-dot"></span>
      <span class="brand-name">brenvaxa</span>
    </div>
    <div class="divider"></div>
    <div class="contact-block">
      <p class="person-name">John Doe</p>
      <p class="person-title">Founder / CEO</p>
      <ul class="contact-list">
        <li class="contact-item">
          <svg class="contact-icon" viewBox="0 0 16 16" aria-hidden="true"><path d="M1 3h14v10H1z M1 3l7 6 7-6" fill="var(--cyan)" stroke="#161616" stroke-width="1.2"/></svg>
          <span>info@brenvaxa.ai</span>
        </li>
        <li class="contact-item">
          <svg class="contact-icon" viewBox="0 0 16 16" aria-hidden="true"><path d="M3.5 1l3 3-1.8 1.8c.8 1.9 2.6 3.7 4.5 4.5L11 8.5l3 3-2 2.5C6.5 13.5 2.5 9.5 1 4z"/></svg>
          <span>(555) 014-2290</span>
        </li>
        <li class="contact-item">
          <svg class="contact-icon" viewBox="0 0 16 16" aria-hidden="true"><circle cx="8" cy="8" r="7"/><path d="M1 8h14M8 1c-3 3.5-3 10.5 0 14M8 1c3 3.5 3 10.5 0 14" fill="none" stroke="#161616" stroke-width="1.1"/></svg>
          <span>https://brenvaxa.ai</span>
        </li>
      </ul>
    </div>
  </section>
</body>
</html>
```